Vault 4 Movie Poster

I need someone to make a movie poster with the pictures provided. You will have complete creative control as long as one picture makes it in. I will pay a fair price if I like it. Feel free to crop and scale and filter and all that. It is starring Owen Harlow, Tom Beasley, Ravi Sethu, and Daniel Prentiss. Produced By Pale Lantern Studios. Directed by Ravi Sethu and Ethan Moreau. it is a medical appocalyptic thriller about people who get addicted to a super drug that was meant to help the disabled but was sold to the public. People get addicted and they try to make their own and turn into a weird kind of mutant creature. No guranteed payment but if I like it I will pay.
It is called Vault 4 Contagion
poster size is 19x28 inches. Top to bottom is longer.Also if you can submit a size that is 9x11 inches that would be great.
Updates
2
days left hurry and get those designs in

```html
<!DOCTYPE html>
<html lang="en">
<head>
<meta charset="utf-8">
<title>Vault 4 Movie Poster</title>
<link href="https://fonts.googleapis.com/css2?family=Stardos+Stencil:wght@700&family=Oswald:wght@300;400&display=swap" rel="stylesheet">
<style>
  :root {
    --page: #ffffff;
    --poster-red: #c8141a;
    --poster-red-deep: #8e0c10;
    --poster-red-hot: #e0221f;
    --ink: #141010;
    --band: #1d1819;
    --credit-red: #d3201f;
    --label-red: #a31418;
  }
  * { margin: 0; padding: 0; box-sizing: border-box; }
  html, body { width: 1200px; height: 1193px; overflow: hidden; background: var(--page); }
  .canvas { position: relative; width: 1200px; height: 1193px; background: var(--page); }

  .poster {
    position: absolute;
    overflow: hidden;
    background:
      radial-gradient(ellipse at 45% 35%, var(--poster-red-hot) 0%, var(--poster-red) 45%, var(--poster-red-deep) 100%);
  }
  .poster--large { left: 0; top: 0; width: 816px; height: 1193px; }
  .poster--small { left: 844px; top: 367px; width: 332px; height: 399px; }

  .poster__still {
    position: absolute;
    transform: rotate(34deg);
    background:
      radial-gradient(ellipse at 35% 45%, #b9806a 0%, #6c4a45 28%, #3a3340 55%, #171314 85%);
    box-shadow: 0 0 40px 20px rgba(20, 10, 10, 0.75);
  }
  .poster--large .poster__still { left: 129px; top: 203px; width: 570px; height: 335px; }
  .poster--small .poster__still { left: 57px; top: 68px; width: 220px; height: 120px; box-shadow: 0 0 12px 6px rgba(20,10,10,0.75); }

  .poster__title {
    position: absolute;
    font-family: "Stardos Stencil", "Courier New", serif;
    font-weight: 700;
    color: var(--ink);
    line-height: 1;
    white-space: nowrap;
  }
  .poster--large .title--top { left: 52px; top: 728px; font-size: 118px; letter-spacing: 4px; }
  .poster--large .title--bottom { left: 105px; top: 856px; font-size: 100px; letter-spacing: 1px; }
  .poster--small .title--top { left: 40px; top: 246px; font-size: 33px; letter-spacing: 1px; }
  .poster--small .title--bottom { left: 44px; top: 289px; font-size: 31px; }

  .poster__crack { position: absolute; left: 0; width: 100%; height: 3px; background: #3a0808; }
  .poster--large .poster__crack { top: 846px; }
  .poster--small .poster__crack { top: 283px; height: 2px; }

  .poster__band {
    position: absolute; left: 0; bottom: 0; width: 100%;
    background: linear-gradient(#2a2224, var(--band) 40%, #0f0c0d);
  }
  .poster--large .poster__band { top: 968px; }
  .poster--small .poster__band { top: 326px; }

  .poster__credits {
    position: absolute; left: 0; width: 100%;
    font-family: "Oswald", "Arial Narrow", sans-serif;
    font-weight: 300;
    color: var(--credit-red);
    text-transform: uppercase;
    text-align: center;
    white-space: nowrap;
  }
  .poster--large .poster__credits { top: 1008px; font-size: 28px; line-height: 46px; }
  .poster--small .poster__credits { top: 336px; font-size: 9px; line-height: 13px; }
  .credits__small { font-size: 0.45em; vertical-align: middle; margin: 0 0.3em; }

  .size-label {
    position: absolute;
    font-family: "Stardos Stencil", "Courier New", serif;
    font-weight: 700;
    font-size: 32px;
    color: var(--label-red);
    white-space: nowrap;
  }
  .size-label--large { left: 848px; top: 46px; }
  .size-label--small { left: 862px; top: 792px; }
</style>
</head>
<body>
<main class="canvas">
  <section class="poster poster--large">
    <div class="poster__still" role="img" aria-label="Film still: a man in a grey t-shirt curled on the floor, tinted dark"></div>
    <h1 class="poster__title title--top">VAULT 4</h1>
    <div class="poster__crack"></div>
    <h1 class="poster__title title--bottom">CONTAGION</h1>
    <div class="poster__band"></div>
    <div class="poster__credits">
      <p><span class="credits__small">STARRING</span>Owen Harlow &nbsp;Tom Beasley &nbsp;Ravi Sethu <span class="credits__small">AND</span> Daniel Prentiss</p>
      <p><span class="credits__small">PRODUCED BY</span>Pale Lantern Studios</p>
      <p><span class="credits__small">DIRECTED BY</span>Ravi Sethu <span class="credits__small">AND</span> Ethan Moreau</p>
    </div>
  </section>

  <p class="size-label size-label--large">19 X 28 INCHES</p>

  <section class="poster poster--small">
    <div class="poster__still" role="img" aria-label="Film still: a man in a grey t-shirt curled on the floor, tinted dark"></div>
    <h2 class="poster__title title--top">VAULT 4</h2>
    <div class="poster__crack"></div>
    <h2 class="poster__title title--bottom">CONTAGION</h2>
    <div class="poster__band"></div>
    <div class="poster__credits">
      <p><span class="credits__small">STARRING</span>Owen Harlow Tom Beasley Ravi Sethu <span class="credits__small">AND</span> Daniel Prentiss</p>
      <p><span class="credits__small">PRODUCED BY</span>Pale Lantern Studios</p>
      <p><span class="credits__small">DIRECTED BY</span>Ravi Sethu <span class="credits__small">AND</span> Ethan Moreau</p>
    </div>
  </section>

  <p class="size-label size-label--small">9 X 11 INCHES</p>
</main>
</body>
</html>
```